Crestline Gas and Plumbing Business Card Design

I am after a business card design for my plumbing business called 'Crestline Gas & Plumbing'. I do all types of plumbing and gas work and specialise in general maintenance plumbing. Would like to see designs using current logo

Industry/Entity Type

Plumbing

Contact Information for Business Card

Name - Dale Whitcombe
Phone number - 0455163027
Email - admin@crestlinegasandplumbing.example.com.au
ABN - 68204915336

```html
<!DOCTYPE html>
<html lang="en">
<head>
<meta charset="utf-8">
<title>Crestline Gas &amp; Plumbing – Business Card</title>
<link rel="stylesheet" href="https://fonts.googleapis.com/css2?family=Arimo:wght@400;700&display=swap">
<style>
  :root {
    --backdrop: #e7e4df;
    --card: #f4f4f4;
    --brand-blue: #253b97;
    --brand-blue-light: #2f7fd0;
    --brand-orange: #e5892a;
    --text-blue: #2a4aa0;
    --rule: #555a66;
  }
  * { margin: 0; padding: 0; box-sizing: border-box; }
  html, body { width: 1200px; height: 800px; overflow: hidden; }
  body {
    background: var(--backdrop);
    font-family: "Arimo", Arial, sans-serif;
    display: flex;
    align-items: center;
    justify-content: center;
    gap: 60px;
  }
  .card {
    position: relative;
    width: 520px;
    height: 297px;
    background: var(--card);
    box-shadow: 0 6px 18px rgba(0,0,0,0.18);
    overflow: hidden;
  }
  .card-wave {
    position: absolute;
    inset: 0;
    width: 100%;
    height: 100%;
  }
  .brand-name {
    position: absolute;
    color: var(--brand-blue);
    font-weight: 700;
    line-height: 1.05;
  }
  .brand-mark {
    display: inline-block;
    width: 14px;
    height: 14px;
    border-radius: 50%;
    background: var(--brand-orange);
    margin-right: 8px;
    vertical-align: middle;
  }
  .card-front .brand-name {
    left: 48px;
    top: 78px;
    font-size: 32px;
    letter-spacing: 0.5px;
  }
  .card-back .brand-name {
    left: 30px;
    top: 190px;
    font-size: 17px;
  }
  .contact {
    position: absolute;
    left: 150px;
    top: 40px;
    color: var(--text-blue);
  }
  .contact-name {
    font-size: 20px;
    font-weight: 700;
  }
  .contact-role {
    font-size: 10px;
    letter-spacing: 5px;
    margin-top: 3px;
    padding-left: 28px;
  }
  .contact-rule {
    width: 62px;
    height: 1px;
    background: var(--rule);
    margin: 4px 0 8px 22px;
  }
  .contact-line {
    display: flex;
    align-items: center;
    font-size: 12px;
    margin-bottom: 6px;
    white-space: nowrap;
  }
  .contact-icon {
    width: 18px;
    height: 18px;
    border-radius: 50%;
    background: var(--brand-orange);
    display: flex;
    align-items: center;
    justify-content: center;
    margin-right: 7px;
    flex: none;
  }
  .contact-abn { padding-left: 25px; }
</style>
</head>
<body>

  <section class="card card-front" aria-label="Card front">
    <svg class="card-wave" viewBox="0 0 520 297" preserveAspectRatio="none" aria-hidden="true">
      <defs>
        <linearGradient id="waveBlueFront" x1="0" y1="1" x2="1" y2="0">
          <stop offset="0" stop-color="#24318e"/>
          <stop offset="0.55" stop-color="#2f7fd0"/>
          <stop offset="1" stop-color="#24318e"/>
        </linearGradient>
      </defs>
      <path d="M0,292 C170,262 330,150 520,62 L520,297 L0,297 Z" fill="var(--brand-orange)"/>
      <path d="M0,297 C180,270 340,160 520,72 L520,297 Z" fill="var(--card)"/>
      <path d="M20,297 C190,275 345,170 520,80 L520,297 Z" fill="url(#waveBlueFront)"/>
    </svg>
    <div class="brand-name"><span class="brand-mark"></span>Crestline<br>Gas &amp; Plumbing</div>
  </section>

  <section class="card card-back" aria-label="Card back">
    <svg class="card-wave" viewBox="0 0 520 297" preserveAspectRatio="none" aria-hidden="true">
      <defs>
        <linearGradient id="waveBlueBack" x1="0" y1="1" x2="1" y2="0">
          <stop offset="0" stop-color="#24318e"/>
          <stop offset="0.55" stop-color="#2f7fd0"/>
          <stop offset="1" stop-color="#24318e"/>
        </linearGradient>
      </defs>
      <path d="M170,297 C300,262 410,200 520,150 L520,297 Z" fill="var(--brand-orange)"/>
      <path d="M200,297 C320,268 420,212 520,164 L520,297 Z" fill="var(--card)"/>
      <path d="M214,297 C330,274 428,222 520,174 L520,297 Z" fill="url(#waveBlueBack)"/>
    </svg>

    <div class="brand-name">Crestline<br>Gas &amp; Plumbing</div>

    <div class="contact">
      <div class="contact-name">Dale Whitcombe</div>
      <div class="contact-role">OWNER</div>
      <div class="contact-rule"></div>
      <div class="contact-line">
        <span class="contact-icon">
          <svg width="8" height="11" viewBox="0 0 8 11" aria-hidden="true"><rect x="0.7" y="0.7" width="6.6" height="9.6" rx="1.2" fill="none" stroke="#fff" stroke-width="1.3"/></svg>
        </span>
        0455 163 027
      </div>
      <div class="contact-line">
        <span class="contact-icon">
          <svg width="11" height="8" viewBox="0 0 11 8" aria-hidden="true"><rect x="0.6" y="0.6" width="9.8" height="6.8" fill="none" stroke="#fff" stroke-width="1.2"/><path d="M0.6,0.6 L5.5,4.5 L10.4,0.6" fill="none" stroke="#fff" stroke-width="1.2"/></svg>
        </span>
        admin@crestlinegasandplumbing.example.com.au
      </div>
      <div class="contact-line contact-abn">ABN - 68204915336</div>
    </div>
  </section>

</body>
</html>
```